Business Card

I need a business card for my work as an energy lawyer. I am a single prctioner and I consult to energy companies regarding a variety of legal issues involving environmental matters, energy efficiency, regulations and contractual arrangements. i need a distinctive business card that stands out and is easy to read. I like bold colors or high contrast. I like a sparse architectural design. The font should be easy to read (many of my clients use reading glasses and are concerned about small type). The card should communicate that I am somewhat different from ordinary legal counsel. Below are some examples of cards that I like. Thank you for your interest and thought. Glen Dusty Harlow
Updates

Thanks to everyone who has submitted a design.  My general comments are:

1.  I like the colourful cards and the high contrast cards.
2.  I prefer the use of icons for home address, phone, mobile and email.
3.  For the high contrast cards please use three colours - black background, and red and white for the logo or information.
4.  The mobile number area code should be 403 and not 404.
5.  I also need to add a direct phone line which is 555-318-2967.

Thank you,

Glen Harlow

Project Deadline Extended
Reason: I have briefly extended the deadline by three days to allow those individuals who responded early to revise their designs based upon the subsequent clarification of the colours (red, white, black background) and the request to use icons and add a direct phone number.

Industry/Entity Type

Business

```html
<!DOCTYPE html>
<html lang="en">
<head>
<meta charset="utf-8">
<title>Glen Dusty Harlow – Business Card</title>
<link href="https://fonts.googleapis.com/css2?family=Arimo:wght@400;700&display=swap" rel="stylesheet">
<style>
  :root {
    --backdrop: #d9d6d2;
    --card: #141414;
    --card-light: #1c1c1c;
    --card-edge: #0c0c0c;
    --red: #d7262e;
    --white: #ffffff;
    --ghost: #222222;
    --icon-glyph: #141414;
  }
  html, body {
    margin: 0;
    padding: 0;
    width: 1200px;
    height: 900px;
    overflow: hidden;
    background: var(--backdrop);
    font-family: "Arimo", Arial, sans-serif;
  }
  .canvas {
    position: relative;
    width: 1200px;
    height: 900px;
  }
  .card {
    position: absolute;
    left: 290px;
    width: 620px;
    height: 354px;
    background: linear-gradient(160deg, var(--card-light) 0%, var(--card) 55%, var(--card-edge) 100%);
    box-shadow: 0 10px 24px rgba(0,0,0,0.3);
    overflow: hidden;
  }
  .card--back { top: 80px; }
  .card--front { top: 466px; }

  /* back side */
  .back-mark {
    position: absolute;
    left: 0; right: 0; top: 50%;
    transform: translateY(-50%);
    display: flex;
    align-items: center;
    justify-content: center;
    gap: 14px;
  }
  .back-mark__dot {
    width: 22px; height: 22px;
    border-radius: 50%;
    background: var(--red);
  }
  .back-mark__name {
    color: var(--red);
    font-weight: 700;
    font-size: 34px;
    letter-spacing: 0.5px;
  }

  /* front side */
  .identity {
    position: absolute;
    top: 38px;
    left: 0; right: 0;
    display: flex;
    justify-content: center;
    align-items: center;
    gap: 14px;
  }
  .identity__dot {
    width: 30px; height: 30px;
    border-radius: 50%;
    border: 2px solid var(--red);
    box-sizing: border-box;
  }
  .identity__name {
    color: var(--red);
    font-weight: 700;
    font-size: 28px;
    line-height: 1;
  }
  .identity__title {
    color: var(--white);
    font-weight: 700;
    font-size: 13px;
    text-align: right;
    margin-top: 6px;
  }

  .ghost-name {
    position: absolute;
    left: 24px;
    bottom: 14px;
    color: var(--ghost);
    font-weight: 700;
    font-size: 48px;
    line-height: 1;
  }

  .contacts {
    position: absolute;
    left: 262px;
    top: 132px;
    list-style: none;
    margin: 0;
    padding: 0;
  }
  .contact {
    display: flex;
    align-items: center;
    gap: 16px;
    margin-bottom: 14px;
    color: var(--white);
    font-weight: 700;
    font-size: 15px;
    line-height: 1.3;
  }
  .contact__icon {
    flex: none;
    width: 30px; height: 30px;
  }
</style>
</head>
<body>
<div class="canvas">

  <section class="card card--back" aria-label="Card back">
    <div class="back-mark">
      <span class="back-mark__dot"></span>
      <span class="back-mark__name">Glen Dusty Harlow</span>
    </div>
  </section>

  <section class="card card--front" aria-label="Card front">
    <div class="ghost-name" aria-hidden="true">Glen Harlow</div>

    <header class="identity">
      <span class="identity__dot"></span>
      <div>
        <div class="identity__name">Glen Dusty Harlow</div>
        <div class="identity__title">Barrister and Solicitor, LLB, ICD.D</div>
      </div>
    </header>

    <ul class="contacts">
      <li class="contact">
        <svg class="contact__icon" viewBox="0 0 30 30" aria-hidden="true">
          <circle cx="15" cy="15" r="14" fill="var(--red)"/>
          <path d="M10 8.5c1-.6 2-.3 2.6.7l1.2 2.1c.4.8.2 1.6-.5 2.1l-1 .7c.8 1.9 2.2 3.4 4.1 4.3l.8-1c.5-.7 1.4-.8 2.1-.4l2 1.3c.9.6 1.1 1.7.5 2.6-1 1.5-2.6 2-4.3 1.3-4-1.7-7.1-5-8.4-9.1-.5-1.7.2-3.5.9-4.6z" fill="var(--icon-glyph)"/>
        </svg>
        <span>1.555.318.2967<br>1.555.604.1183</span>
      </li>
      <li class="contact">
        <svg class="contact__icon" viewBox="0 0 30 30" aria-hidden="true">
          <circle cx="15" cy="15" r="14" fill="var(--red)"/>
          <rect x="8" y="10" width="14" height="10" rx="1" fill="none" stroke="var(--icon-glyph)" stroke-width="1.8"/>
          <path d="M8.5 10.5 15 16l6.5-5.5" fill="none" stroke="var(--icon-glyph)" stroke-width="1.8"/>
        </svg>
        <span>email: dusty@harlowcounsel.example</span>
      </li>
      <li class="contact">
        <svg class="contact__icon" viewBox="0 0 30 30" aria-hidden="true">
          <circle cx="15" cy="15" r="14" fill="var(--red)"/>
          <path d="M15 7a5.5 5.5 0 0 0-5.5 5.5c0 4 5.5 10.5 5.5 10.5s5.5-6.5 5.5-10.5A5.5 5.5 0 0 0 15 7z" fill="var(--icon-glyph)"/>
          <circle cx="15" cy="12.5" r="2" fill="var(--red)"/>
        </svg>
        <span>418 Ridgeview Lane S.W., Calgary, Alberta</span>
      </li>
    </ul>
  </section>

</div>
</body>
</html>
```